Business Card Design

I would like a new business card for my business Drive Haven, we operate within the automotive industry and offer customer retention solutions for independent mechanical workshops across Australia and New Zealand. The program incorporates service reminders and roadside assistance for consumers and is designed to get the client back for their vehicle service visit, I would like a doubled sided design that incorporates my logos and a two tone type card that has white and a carbon fibre look also use the blue in the logo I have uploaded. It would be great to have icons as the phone/fax/email etc details for the card are below. The finished design must be a print ready file useable.It would be great if the design could communicate the what type of business we are
Marcus Trelby
General Manager
Drive Haven Pty Ltd
Unit 5/42 Corrin Street
Wexmoor Newcastle NSW 2391
Ph:+61240173500
fax:+61240173600
Mobile:0415889214
Email:info@drivehaven-example.com.au
Updates
I have just upload a carbon fibre background for the business card hope it helps
Hello guys I am sorry fr no feedback I have been away over seas I will send feedback when I return monday
Industry/Entity Type
Automotive
Look and feel

```html
<!DOCTYPE html>
<html lang="en">
<head>
<meta charset="utf-8">
<title>Drive Haven — Business Card</title>
<link href="https://fonts.googleapis.com/css2?family=Open+Sans:wght@400;600;700&display=swap" rel="stylesheet">
<style>
  :root {
    --bg: #d9d9d9;
    --white: #ffffff;
    --blue: #1e96d8;
    --blue-dark: #137cc0;
    --carbon-1: #2a2a2c;
    --carbon-2: #151516;
    --ink: #2f3237;
    --silver: #c9ced3;
    --text-light: #f2f4f6;
  }
  * { margin: 0; padding: 0; box-sizing: border-box; }
  html, body { width: 1200px; height: 900px; overflow: hidden; }
  body {
    background: var(--bg);
    font-family: "Open Sans", Arial, sans-serif;
    position: relative;
  }
  .card {
    position: absolute;
    width: 640px;
    height: 390px;
    background: var(--white);
    overflow: hidden;
    box-shadow: 0 6px 18px rgba(0,0,0,0.25);
  }
  .card--front { left: 150px; top: 40px; }
  .card--back  { left: 410px; top: 470px; }

  .carbon {
    position: absolute;
    left: 0; width: 100%;
    background: linear-gradient(180deg, var(--carbon-1), var(--carbon-2));
  }
  .blue-rule { position: absolute; left: 0; width: 100%; height: 6px; background: var(--blue); }

  /* front */
  .front-top { top: 0; height: 64px; }
  .front-top-rule { top: 64px; }
  .front-bottom-rule { top: 292px; }
  .front-bottom { top: 298px; height: 92px; }
  .brand {
    position: absolute;
    display: flex; align-items: center; gap: 18px;
    font-weight: 700; color: var(--ink);
  }
  .brand__dot { border-radius: 50%; background: var(--blue); flex: none; }
  .front-brand { left: 90px; top: 138px; font-size: 60px; letter-spacing: 1px; }
  .front-brand .brand__dot { width: 64px; height: 64px; }
  .badge { position: absolute; }
  .front-badge { right: 10px; top: 6px; width: 104px; height: 104px; }

  /* back */
  .back-brand { left: 40px; top: 40px; font-size: 46px; }
  .back-brand .brand__dot { width: 54px; height: 54px; }
  .name-band {
    position: absolute; left: 0; top: 150px; width: 100%; height: 62px;
    background: linear-gradient(90deg, var(--blue-dark), var(--blue));
    display: flex; align-items: center; padding-left: 30px;
    color: var(--white);
  }
  .name-band__name { font-weight: 700; font-size: 22px; }
  .name-band__sep { margin: 0 10px; font-size: 22px; font-weight: 400; }
  .name-band__title { font-size: 15px; font-weight: 400; }
  .back-carbon { top: 212px; height: 120px; }
  .contacts {
    position: absolute; left: 28px; top: 226px;
    list-style: none; color: var(--text-light); font-size: 15px; line-height: 22px;
  }
  .contacts li { display: flex; align-items: center; gap: 10px; }
  .contacts svg { width: 14px; height: 14px; flex: none; }
  .address-band {
    position: absolute; left: 0; top: 332px; width: 100%; height: 58px;
    background: var(--blue);
    color: var(--white); font-size: 16px;
    display: flex; align-items: center; padding-left: 150px;
  }
  .back-badge { right: 40px; top: 50px; width: 200px; height: 200px; }
</style>
</head>
<body>

<section class="card card--front" aria-label="Business card front">
  <div class="carbon front-top" role="img" aria-label="Carbon fibre texture band"></div>
  <div class="blue-rule front-top-rule"></div>
  <div class="brand front-brand"><span class="brand__dot"></span>Drive Haven</div>
  <div class="blue-rule front-bottom-rule"></div>
  <div class="carbon front-bottom" role="img" aria-label="Carbon fibre texture band"></div>
  <svg class="badge front-badge" viewBox="0 0 100 100" aria-hidden="true">
    <circle cx="50" cy="50" r="48" fill="var(--white)"/>
    <circle cx="50" cy="50" r="44" fill="var(--blue)"/>
    <circle cx="50" cy="50" r="30" fill="var(--silver)"/>
  </svg>
</section>

<section class="card card--back" aria-label="Business card back">
  <div class="brand back-brand"><span class="brand__dot"></span>Drive Haven</div>
  <div class="name-band">
    <span class="name-band__name">Marcus Trelby</span>
    <span class="name-band__sep">|</span>
    <span class="name-band__title">General Manager</span>
  </div>
  <div class="carbon back-carbon" role="img" aria-label="Carbon fibre texture panel"></div>
  <ul class="contacts">
    <li><svg viewBox="0 0 16 16"><rect width="16" height="16" rx="2" fill="#fff"/><path d="M4 3l2 0 1 3-1.5 1a6 6 0 0 0 3.5 3.5L10 9l3 1v2c0 1-1 1-1 1A9 9 0 0 1 3 4s0-1 1-1z" fill="#222"/></svg>+61240173500</li>
    <li><svg viewBox="0 0 16 16"><rect width="16" height="16" rx="2" fill="#fff"/><rect x="3" y="6" width="10" height="7" fill="#222"/><rect x="5" y="2" width="6" height="5" fill="#222"/><rect x="6" y="3" width="4" height="3" fill="#fff"/></svg>+61240173600</li>
    <li><svg viewBox="0 0 16 16"><rect width="16" height="16" rx="2" fill="#fff"/><rect x="5" y="2" width="6" height="12" rx="1" fill="#222"/><rect x="6" y="3.5" width="4" height="7" fill="#fff"/></svg>0415889214</li>
    <li><svg viewBox="0 0 16 16"><rect width="16" height="16" rx="2" fill="#fff"/><rect x="2.5" y="4" width="11" height="8" fill="#222"/><path d="M2.5 4l5.5 4.5L13.5 4" stroke="#fff" fill="none"/></svg>info@drivehaven-example.com.au</li>
  </ul>
  <div class="address-band">Unit 5/42 Corrin Street, Wexmoor Newcastle NSW 2391</div>
  <svg class="badge back-badge" viewBox="0 0 100 100" aria-hidden="true">
    <circle cx="50" cy="50" r="49" fill="var(--white)"/>
    <circle cx="50" cy="50" r="45" fill="var(--blue)"/>
    <circle cx="50" cy="50" r="30" fill="var(--silver)"/>
  </svg>
</section>

</body>
</html>
```